Derya & Kerem Wedding Invitation and Decorative Designs

We are looking for a sweet and elegant design for our wedding invitation. We need different versions of the same design to use both as printed hard copies and in digital formats (WhatsApp image, instagram post, etc) Please see attached sample invitation, which we like as a simple and elegant option, but also find it quite basic. We are open to creative suggestions following a similar style.
Once we decide on an invitation design, we would like to use the same design elements in guest name cards, welcome sign, menu cards and print cover for the dance floor of our wedding venue. Please see random samples of these materials attached. We also attach a photo from our wedding venue displaying a close to final visual of the decoration we chose for our wedding day (sharing in case it helps as an inspiration source and helps with matching decoration colors with the designs)
Requirements
Must have
- Must have a style similar to the attached sample invitation

```html
<!DOCTYPE html>
<html lang="en">
<head>
<meta charset="utf-8">
<title>Derya &amp; Kerem — Wedding Invitation</title>
<link rel="stylesheet" href="https://fonts.googleapis.com/css2?family=Great+Vibes&display=swap">
<style>
  :root {
    --backdrop: #f4f4f2;
    --card-top: #c6c8c7;
    --card-bottom: #cfd0cd;
    --fold-line: #e2e3e0;
    --ink: #141414;
    --bloom-rose: #b23f5c;
    --bloom-teal: #5f9aa3;
    --bloom-cream: #e9e2dc;
    --frame-gold: #d7a13a;
  }
  * { margin: 0; padding: 0; box-sizing: border-box; }
  html, body {
    width: 1200px;
    height: 1200px;
    overflow: hidden;
    background: var(--backdrop);
  }
  .invitation {
    position: absolute;
    left: 170px;
    top: 110px;
    width: 860px;
    height: 980px;
    display: flex;
    flex-direction: column;
    box-shadow: 0 6px 22px rgba(0,0,0,0.12);
  }
  .invitation__cover {
    position: relative;
    height: 420px;
    background: var(--card-top);
    border-bottom: 2px solid var(--fold-line);
  }
  .wreath {
    position: absolute;
    left: 50%;
    top: 24px;
    width: 360px;
    height: 376px;
    transform: translateX(-50%);
  }
  .wreath__art {
    position: absolute;
    inset: 0;
  }
  .monogram {
    position: absolute;
    inset: 0;
    display: flex;
    flex-direction: column;
    align-items: center;
    justify-content: center;
    font-family: "Great Vibes", cursive;
    color: var(--ink);
    line-height: 1;
  }
  .monogram__name { font-size: 52px; }
  .monogram__amp { font-size: 28px; margin: 2px 0; }
  .invitation__inside {
    flex: 1;
    background: var(--card-bottom);
    display: flex;
    flex-direction: column;
    align-items: center;
    justify-content: center;
    padding-bottom: 70px;
  }
  .couple {
    font-family: "Great Vibes", cursive;
    font-weight: 400;
    color: var(--ink);
    text-align: center;
    font-size: 118px;
    line-height: 128px;
  }
  .couple span { display: block; }
</style>
</head>
<body>
  <main class="invitation">
    <section class="invitation__cover">
      <div class="wreath">
        <svg class="wreath__art" viewBox="0 0 360 376" role="img" aria-label="Watercolour floral wreath of rose and cream blossoms with teal leaves around a thin gold geometric frame">
          <defs>
            <linearGradient id="bloomGradient" x1="0" y1="0" x2="1" y2="1">
              <stop offset="0" stop-color="var(--bloom-rose)" stop-opacity="0.55"/>
              <stop offset="0.5" stop-color="var(--bloom-teal)" stop-opacity="0.45"/>
              <stop offset="1" stop-color="var(--bloom-rose)" stop-opacity="0.55"/>
            </linearGradient>
          </defs>
          <ellipse cx="180" cy="188" rx="148" ry="160" fill="none" stroke="url(#bloomGradient)" stroke-width="34"/>
        </svg>
        <div class="monogram">
          <span class="monogram__name">Derya</span>
          <span class="monogram__amp">&amp;</span>
          <span class="monogram__name">Kerem</span>
        </div>
      </div>
    </section>
    <section class="invitation__inside">
      <h1 class="couple">
        <span>Derya</span>
        <span>Weds</span>
        <span>Kerem</span>
      </h1>
    </section>
  </main>
</body>
</html>
```